MD Trailcraft & Wildland Fair

I need a 1 page flyer for promotion of an upcoming sportsman and outdoor show(expo). would like the flyer to be able to be printed in B&W and color! show will include all things to do with the out doors, hunting fishing boating hiking atv camping rvs motorcycles. the event will have a kids zone, events games and activities for kids. there will be vendors showing the newest products. guest speakers and industry experts giving training and advice. this show will have something for everyone. food trucks and concessions. 200+ vendors. waterfould calling competition. deer/buck scoring casting competition for kids 3D Archery competitions

Target Market(s)

anyone event open to all ages!

Colors
ec1f27
000000
fbed22

Requirements
Must have
• date- september 1-2 2018
• location Pelling valley expo 4837 orchardmill rd east calverton MD 21652
• facebook - mdtrailcraftfair
• email mdtrailcraftfair@quorvex.com
• web www.mdtrailcraftfair.com
• vendor spaces still available! sign up now space going fast
Nice to have
• would like some thing that can be both printed in B&W and Color, and still have a great affect.
Should not have
• open to any suggestions

```html
<!DOCTYPE html>
<html lang="en">
<head>
<meta charset="utf-8">
<title>MD Trailcraft &amp; Wildland Fair – Flyer</title>
<link rel="stylesheet" href="https://fonts.googleapis.com/css2?family=Lato:wght@400;700;900&family=Roboto:wght@500;700&family=Raleway:wght@700&display=swap">
<style>
  :root {
    --page: #ffffff;
    --ink: #1a1a1a;
    --red: #ec1f27;
    --yellow: #fbed22;
    --pale-yellow: #fdf6a8;
    --photo-tone: #eef3a2;
    --grey-dark: #6b6b6b;
    --grey-mid: #8a8a8a;
    --grey-light: #e4e4e4;
  }
  * { margin: 0; padding: 0; box-sizing: border-box; }
  html, body { width: 1200px; height: 1200px; overflow: hidden; background: var(--page); }
  body { position: relative; font-family: "Lato", sans-serif; color: var(--ink); }

  .flyer {
    --accent: var(--red);
    --band: var(--yellow);
    --title: var(--red);
    --sign-box: var(--red);
    --sign-text: var(--yellow);
    --sign-small: var(--pale-yellow);
    --divider: var(--yellow);
    --photo: var(--photo-tone);
    position: absolute;
    width: 602px; height: 850px;
    background: var(--page);
    overflow: hidden;
    border: 1px solid #e6e6e6;
  }
  .flyer--colour { left: 26px; top: 38px; }
  .flyer--mono {
    left: 658px; top: 450px;
    transform: scale(0.8405); transform-origin: 0 0;
    --accent: var(--grey-mid);
    --band: var(--grey-light);
    --title: var(--grey-dark);
    --sign-box: var(--grey-dark);
    --sign-text: #ffffff;
    --sign-small: #f0f0f0;
    --divider: var(--grey-light);
    --photo: #dcdcdc;
  }

  .event-date { position: absolute; left: 30px; top: 36px; }
  .event-date__days { font-weight: 900; font-size: 17px; }
  .event-date__year {
    font-family: "Raleway", sans-serif; font-weight: 700;
    font-size: 36px; letter-spacing: 7px; line-height: 36px; color: var(--accent);
  }
  .venue { position: absolute; left: 30px; top: 92px; font-size: 14px; line-height: 20px; }

  .title-band {
    position: absolute; left: 0; top: 178px; width: 100%; height: 62px;
    background: var(--band); display: flex; align-items: center; padding-left: 28px;
  }
  .title-band__name {
    font-family: "Raleway", sans-serif; font-weight: 700; font-size: 31px;
    color: var(--title); white-space: nowrap;
  }

  .offer { position: absolute; left: 34px; top: 296px; font-weight: 900; font-size: 16.5px; line-height: 20px; width: 540px; }

  .product-photo {
    position: absolute; left: 0; top: 390px; width: 100%; height: 367px;
    background:
      radial-gradient(ellipse 170px 130px at 100px 250px, var(--photo) 0%, transparent 100%),
      radial-gradient(ellipse 160px 150px at 450px 130px, #e4e4e4 0%, transparent 100%);
    opacity: 0.9;
  }

  .products { position: absolute; top: 346px; font-size: 13.5px; line-height: 20px; list-style: none; }
  .products--a { left: 34px; }
  .products--b { left: 220px; }
  .products--c { left: 378px; }
  .products--d { left: 505px; }
  .col-divider {
    position: absolute; top: 346px; height: 160px; width: 0;
    border-left: 2px dashed var(--divider);
  }
  .col-divider--1 { left: 204px; }
  .col-divider--2 { left: 362px; }
  .col-divider--3 { left: 492px; }

  .signup { position: absolute; left: 0; top: 440px; width: 602px; height: 317px; }
  .signup__box { position: absolute; left: 0; top: 0; }
  .signup__text { position: absolute; left: 232px; top: 196px; width: 364px; text-align: center; font-family: "Roboto", sans-serif; }
  .signup__small { font-weight: 500; font-size: 13px; color: var(--sign-small); letter-spacing: 0.3px; }
  .signup__big { font-weight: 700; font-size: 31px; line-height: 35px; color: var(--sign-text); }

  .contact-band {
    position: absolute; left: 0; top: 757px; width: 100%; height: 93px;
    background: var(--band); padding: 14px 22px 0;
  }
  .contact-band__heading { font-weight: 900; font-size: 16.5px; }
  .contact-list { display: flex; align-items: center; margin-top: 12px; list-style: none; font-size: 11px; }
  .contact-list__item { display: flex; align-items: center; gap: 6px; padding: 0 14px; height: 26px; }
  .contact-list__item:first-child { padding-left: 0; }
  .contact-list__item + .contact-list__item { border-left: 1.5px solid #333; }
  .icon { width: 15px; height: 15px; flex: none; }
  .social-dot { width: 13px; height: 13px; border-radius: 50%; background: var(--accent); flex: none; }
</style>
</head>
<body>

<section class="flyer flyer--colour">
  <div class="event-date">
    <p class="event-date__days">September 1-2</p>
    <p class="event-date__year">2018</p>
  </div>
  <p class="venue">&nbsp;Pelling valley expo 4837<br>orchardmill rd east calverton<br>MD 21652</p>
  <div class="title-band"><h1 class="title-band__name">MD TRAILCRAFT &amp; WILDLAND FAIR</h1></div>

  <h2 class="offer">Over 60,000 sqft of INDOOR and 30,000+ sqft OUTDOOR products and services including:</h2>

  <div class="product-photo" role="img" aria-label="Faded photo of a camping tent and a motorcycle"></div>

  <ul class="products products--a"><li>*Sports Equipment</li><li>*Tackle &amp; Bait</li><li>*Taxidermists</li><li>*Charter Boats</li><li>*Trailers</li><li>* Outdoor Magazines</li><li>*Camping Equipment</li><li>* and much more...</li></ul>
  <ul class="products products--b"><li>*Campers</li><li>*Motorcycles</li><li>*Outfitters</li><li>*Golf Resorts</li><li>*Sporting Clubs</li><li>*Camp Grounds</li><li>* Hunting Supplies</li></ul>
  <ul class="products products--c"><li>*Boats</li><li>*ATV's</li><li>*Guns</li><li>*Knives</li><li>*Game Calls</li></ul>
  <ul class="products products--d"><li>*RV's</li><li>*Trucks</li><li>*Jet Skis</li><li>*Archery</li></ul>
  <span class="col-divider col-divider--1"></span>
  <span class="col-divider col-divider--2"></span>
  <span class="col-divider col-divider--3"></span>

  <div class="signup">
    <svg class="signup__box" width="602" height="317" viewBox="0 0 602 317" aria-hidden="true">
      <path d="M228,180 L578,104 Q596,100 598,118 L610,330 L214,330 L214,196 Q214,183 228,180 Z" fill="var(--sign-box)"/>
    </svg>
    <div class="signup__text">
      <p class="signup__small">VENDOR SPACES STILL AVAILABLE!</p>
      <p class="signup__big">SIGN UP NOW!<br>SPACE GOING FAST!</p>
    </div>
  </div>

  <footer class="contact-band">
    <h3 class="contact-band__heading">Contact us today:</h3>
    <ul class="contact-list">
      <li class="contact-list__item"><span class="social-dot"></span>mdtrailcraftfair</li>
      <li class="contact-list__item">
        <svg class="icon" viewBox="0 0 16 16" aria-hidden="true"><rect x="1" y="3" width="14" height="10" fill="var(--accent)"/><polyline points="1,3 8,9 15,3" fill="none" stroke="#fff" stroke-width="1.3"/></svg>
        mdtrailcraftfair@quorvex.com</li>
      <li class="contact-list__item">
        <svg class="icon" viewBox="0 0 16 16" aria-hidden="true"><g fill="none" stroke="var(--accent)" stroke-width="1.4"><circle cx="8" cy="8" r="6.5"/><ellipse cx="8" cy="8" rx="3" ry="6.5"/><line x1="1.5" y1="8" x2="14.5" y2="8"/></g></svg>
        www.mdtrailcraftfair.com</li>
    </ul>
  </footer>
</section>

<section class="flyer flyer--mono">
  <div class="event-date">
    <p class="event-date__days">September 1-2</p>
    <p class="event-date__year">2018</p>
  </div>
  <p class="venue">&nbsp;Pelling valley expo 4837<br>orchardmill rd east calverton<br>MD 21652</p>
  <div class="title-band"><h1 class="title-band__name">MD TRAILCRAFT &amp; WILDLAND FAIR</h1></div>

  <h2 class="offer">Over 60,000 sqft of INDOOR and 30,000+ sqft OUTDOOR products and services including:</h2>

  <div class="product-photo" role="img" aria-label="Faded greyscale photo of a camping tent and a motorcycle"></div>

  <ul class="products products--a"><li>*Sports Equipment</li><li>*Tackle &amp; Bait</li><li>*Taxidermists</li><li>*Charter Boats</li><li>*Trailers</li><li>* Outdoor Magazines</li><li>*Camping Equipment</li><li>* and much more...</li></ul>
  <ul class="products products--b"><li>*Campers</li><li>*Motorcycles</li><li>*Outfitters</li><li>*Golf Resorts</li><li>*Sporting Clubs</li><li>*Camp Grounds</li><li>* Hunting Supplies</li></ul>
  <ul class="products products--c"><li>*Boats</li><li>*ATV's</li><li>*Guns</li><li>*Knives</li><li>*Game Calls</li></ul>
  <ul class="products products--d"><li>*RV's</li><li>*Trucks</li><li>*Jet Skis</li><li>*Archery</li></ul>
  <span class="col-divider col-divider--1"></span>
  <span class="col-divider col-divider--2"></span>
  <span class="col-divider col-divider--3"></span>

  <div class="signup">
    <svg class="signup__box" width="602" height="317" viewBox="0 0 602 317" aria-hidden="true">
      <path d="M228,180 L578,104 Q596,100 598,118 L610,330 L214,330 L214,196 Q214,183 228,180 Z" fill="var(--sign-box)"/>
    </svg>
    <div class="signup__text">
      <p class="signup__small">VENDOR SPACES STILL AVAILABLE!</p>
      <p class="signup__big">SIGN UP NOW!<br>SPACE GOING FAST!</p>
    </div>
  </div>

  <footer class="contact-band">
    <h3 class="contact-band__heading">Contact us today:</h3>
    <ul class="contact-list">
      <li class="contact-list__item"><span class="social-dot"></span>mdtrailcraftfair</li>
      <li class="contact-list__item">
        <svg class="icon" viewBox="0 0 16 16" aria-hidden="true"><rect x="1" y="3" width="14" height="10" fill="var(--accent)"/><polyline points="1,3 8,9 15,3" fill="none" stroke="#fff" stroke-width="1.3"/></svg>
        mdtrailcraftfair@quorvex.com</li>
      <li class="contact-list__item">
        <svg class="icon" viewBox="0 0 16 16" aria-hidden="true"><g fill="none" stroke="var(--accent)" stroke-width="1.4"><circle cx="8" cy="8" r="6.5"/><ellipse cx="8" cy="8" rx="3" ry="6.5"/><line x1="1.5" y1="8" x2="14.5" y2="8"/></g></svg>
        www.mdtrailcraftfair.com</li>
    </ul>
  </footer>
</section>

</body>
</html>
```